Clone http://www.pebbledeskwriter.com/ (fully functioning WordPress website - not just design)

1) Clone or recreate http://www.pebbledeskwriter.com/ in Wordpress with WooCommerece plugin
2) Connect to our Existing Quendo Account
3) Make site-wide text only changes that we provide you when site is complete.

We will provide all the graphics according to your size requirements.

Cash awarded to the closest copy of http://www.pebbledeskwriter.com/

Target Market(s)

WordPress developer

Number of Pages Required

5+ page

Font styles to use
Sans Serif

Colors
abd037
cadf82
eaf2ce

Requirements
Must have
• Fully functioning website.

```html
<!DOCTYPE html>
<html lang="en">
<head>
<meta charset="utf-8">
<title>Larkspur Merge – Easy, Online Mail Merge</title>
<link href="https://fonts.googleapis.com/css2?family=Roboto:wght@300;400;500&display=swap" rel="stylesheet">
<style>
:root{
  --green:#8cc13f;
  --wood-dark:#4a200d;
  --wood:#6b3419;
  --wood-light:#7d4020;
  --ink:#222222;
  --text:#555555;
  --grey-band:#f5f5f5;
  --footer:#2b2a30;
  --footer-bar:#232228;
  --white:#ffffff;
  --line:#dddddd;
  --blue:#2d9fd8;
  --red:#e0342f;
  --navy:#3b5da8;
}
*{box-sizing:border-box;margin:0;padding:0}
html,body{width:1200px;height:2711px;overflow:hidden;background:var(--white)}
body{font-family:"Roboto",Arial,sans-serif;color:var(--text);position:relative}

/* hero */
.hero{position:absolute;left:0;top:0;width:1200px;height:609px;
  background:linear-gradient(100deg,var(--wood-dark) 0%,var(--wood) 35%,var(--wood-light) 60%,var(--wood) 100%)}
.brand{position:absolute;left:90px;top:60px;font-size:26px;font-weight:400;color:var(--white);letter-spacing:.5px}
.nav{position:absolute;left:0;top:0;font-size:12px;font-weight:400;color:var(--white);text-transform:uppercase}
.nav a{position:absolute;top:67px;white-space:nowrap;color:inherit;text-decoration:none}
.nav .active{color:var(--green)}
.nav .active::before{content:"";position:absolute;left:-8px;right:-8px;top:-23px;height:2px;background:var(--green)}
.btn-login{position:absolute;left:941px;top:60px;width:75px;height:29px;background:var(--green);color:var(--white);font-size:12px;font-weight:400;display:flex;align-items:center;justify-content:center}
.btn-register{position:absolute;left:1021px;top:58px;width:90px;height:31px;border:2px solid var(--white);color:var(--white);font-size:12px;font-weight:400;display:flex;align-items:center;justify-content:center}
.hero-kicker{position:absolute;left:87px;top:242px;font-size:41px;font-weight:300;color:var(--white)}
.hero-title{position:absolute;left:85px;top:290px;font-size:66px;font-weight:300;color:var(--white);line-height:1}
.btn-trial{position:absolute;left:89px;top:367px;width:171px;height:40px;background:var(--green);color:var(--white);font-size:12px;font-weight:400;display:flex;align-items:center;justify-content:center;text-transform:uppercase}
.hero-note{position:absolute;left:89px;top:421px;font-size:12px;color:var(--white)}
.hero-art{position:absolute;left:565px;top:210px;width:560px;height:399px;
  background:linear-gradient(180deg,rgba(240,240,240,.18) 0%,rgba(45,159,216,.35) 100%);border-radius:6px 6px 0 0}
.scroll-down{position:absolute;left:584px;top:591px;width:36px;height:36px;border-radius:50%;background:var(--white);box-shadow:0 2px 5px rgba(0,0,0,.25)}

/* intro */
.intro-title{position:absolute;left:0;width:1200px;top:712px;text-align:center;font-size:31px;font-weight:300;color:var(--ink);line-height:40px;text-transform:uppercase}
.divider{position:absolute;left:575px;top:799px;width:50px;height:1px;background:#bbbbbb}
.intro-text{position:absolute;left:170px;width:860px;top:814px;text-align:center;font-size:13px;line-height:22px}
.btn-outline{position:absolute;border:1px solid var(--line);color:var(--ink);font-size:11px;font-weight:400;display:flex;align-items:center;justify-content:center;text-transform:uppercase;background:var(--white)}
.easier{position:absolute;left:0;width:1200px;top:978px;text-align:center;font-size:31px;font-weight:500;color:var(--green);text-transform:uppercase}

/* steps */
.band-grey{position:absolute;left:0;top:1386px;width:1200px;height:417px;background:var(--grey-band)}
.step-num{position:absolute;font-size:60px;font-weight:500;color:var(--green);line-height:1}
.step-num::after{content:"";position:absolute;left:-6px;top:52px;width:50px;height:2px;background:var(--green);transform:rotate(18deg);transform-origin:left}
.step-title{position:absolute;font-size:31px;font-weight:300;color:var(--ink);text-transform:uppercase;line-height:1.1}
.step-sub{position:absolute;font-size:14px;font-weight:500;color:var(--ink)}
.step-text{position:absolute;width:425px;font-size:13px;line-height:23px;hyphens:auto;-webkit-hyphens:auto}
.step-art{position:absolute;border-radius:8px}

/* cta */
.cta{position:absolute;left:0;top:2201px;width:1200px;height:322px;background:var(--green)}
.cta-title{position:absolute;left:0;width:1200px;top:93px;text-align:center;font-size:31px;font-weight:300;color:var(--white);text-transform:uppercase}
.cta-text{position:absolute;left:133px;width:934px;top:149px;text-align:center;font-size:13px;line-height:20px;color:var(--white)}
.cta .btn-outline{left:510px;top:202px;width:182px;height:44px;border:none}

/* footer */
.footer{position:absolute;left:0;top:2523px;width:1200px;height:142px;background:var(--footer)}
.footer-brand{position:absolute;left:90px;top:2582px;font-size:20px;font-weight:400;color:var(--white)}
.footer-nav a{position:absolute;top:2578px;font-size:11px;font-weight:400;color:var(--white);text-transform:uppercase;white-space:nowrap;text-decoration:none}
.footer-rule{position:absolute;left:470px;top:2609px;width:641px;height:1px;background:#44434a}
.social{position:absolute;top:2621px;width:26px;height:26px;border-radius:50%}
.footer-bar{position:absolute;left:0;top:2665px;width:1200px;height:46px;background:var(--footer-bar)}
.copyright{position:absolute;left:90px;top:2683px;font-size:11px;font-weight:500;color:var(--white)}
.legal a{position:absolute;top:2683px;font-size:11px;font-weight:500;color:var(--white);white-space:nowrap;text-decoration:none}
.to-top{position:absolute;left:1146px;top:2655px;width:28px;height:28px;border-radius:50%;background:var(--green)}
</style>
</head>
<body>

<header class="hero" role="img" aria-label="Dark wooden desk surface background"></header>
<div class="brand">Larkspur</div>
<nav class="nav">
  <a class="active" style="left:535px">Home</a>
  <a style="left:608px">Tour</a>
  <a style="left:677px">Price</a>
  <a style="left:750px">Our Team</a>
  <a style="left:847px">Contact Us</a>
</nav>
<div class="btn-login">LOGIN</div>
<div class="btn-register">REGISTER</div>

<h2 class="hero-kicker">Easy, Online</h2>
<h1 class="hero-title">Mail Merge</h1>
<div class="btn-trial">Start a free trial</div>
<p class="hero-note">Start building your mail merge online now!</p>
<div class="hero-art" role="img" aria-label="Illustration of hands typing on a laptop with phone, ruler, pencil, mouse and tablet on a desk"></div>
<div class="scroll-down">
  <svg width="36" height="36" viewBox="0 0 36 36"><path d="M15 16.5l3 3 3-3" fill="none" stroke="#333" stroke-width="1.6"/></svg>
</div>

<h2 class="intro-title">Do you have a letter you<br>need to send out to multiple people?</h2>
<div class="divider"></div>
<p class="intro-text">Lorem ipsum dolor sit amet, consectetuer adipiscing elit. Aenean commodo ligula eget dolor aenean massa. Cum sociis natoque penatibus et magnis dis parturient montes, nascetur ridiculus mus donec quam felis ultricies .</p>
<div class="btn-outline" style="left:537px;top:880px;width:126px;height:38px">Learn more</div>
<h2 class="easier">100% easier than using Quillpad Docs!</h2>

<div class="step-num" style="left:98px;top:1124px">1</div>
<h3 class="step-title" style="left:157px;top:1122px">Upload your data</h3>
<p class="step-sub" style="left:158px;top:1158px">Create a list of addresses, names or other data</p>
<p class="step-text" style="left:160px;top:1190px">Lorem ipsum dolor sit amet consectetuer adipiscing elit. Aenean commodo ligula eget dolor aenean massa. Cum sociis natoque penatibus et magnis dis parturient montes nascetur ridiculus mus. Donec quam felis ultricies nec pellentesque eu pretium quis sem. Nulla consequat massa quis enim.</p>
<div class="step-art" style="left:696px;top:1106px;width:274px;height:177px;background:linear-gradient(180deg,#e6e6e6 0%,#d5e8f3 60%,#1c8fd0 100%)" role="img" aria-label="Cloud upload illustration"></div>

<div class="band-grey"></div>
<div class="step-art" style="left:206px;top:1482px;width:237px;height:235px;background:linear-gradient(180deg,#37424a 0%,#37424a 20%,#dedede 20%,#cfcfcf 100%);border-radius:4px" role="img" aria-label="Browser window with keyboard illustration"></div>
<div class="step-num" style="left:630px;top:1514px">2</div>
<h3 class="step-title" style="left:688px;top:1513px">Design your template</h3>
<p class="step-sub" style="left:690px;top:1549px">Build your document in your browser, it's easy</p>
<p class="step-text" style="left:690px;top:1581px">Lorem ipsum dolor sit amet consectetuer adipiscing elit. Aenean commodo ligula eget dolor aenean massa. Cum sociis natoque penatibus et magnis dis parturient montes nascetur ridiculus mus. Donec quam felis ultricies nec pellentesque eu pretium quis sem. Nulla consequat massa quis enim.</p>

<div class="step-num" style="left:98px;top:1926px">3</div>
<h3 class="step-title" style="left:157px;top:1922px">Merge to PDF</h3>
<p class="step-sub" style="left:158px;top:1958px">Combine it all into a PDF ready for print</p>
<p class="step-text" style="left:160px;top:1990px">Lorem ipsum dolor sit amet consectetuer adipiscing elit. Aenean commodo ligula eget dolor aenean massa. Cum sociis natoque penatibus et magnis dis parturient montes nascetur ridiculus mus. Donec quam felis ultricies nec pellentesque eu pretium quis sem. Nulla consequat massa quis enim.</p>
<div class="step-art" style="left:746px;top:1888px;width:212px;height:241px;background:linear-gradient(180deg,#e4e4e4 0%,#e4e4e4 35%,#ee5a40 35%,#ee5a40 62%,#e4e4e4 62%,#e4e4e4 100%)" role="img" aria-label="PDF document file illustration"></div>

<section class="cta">
  <h2 class="cta-title">Start building your mail merge online now!</h2>
  <p class="cta-text">Lorem ipsum dolor sit amet, consectetuer adipiscing elit. Aenean commodo ligula eget dolor. Cum sociis natoque penatibus et magnis dis parturient montes nascetur ridiculus mus. Donec quam felis, ultricies nec, pellentesque eu, pretium quis, sem.</p>
  <div class="btn-outline">Start your free trial</div>
</section>

<div class="footer"></div>
<div class="footer-brand">Larkspur</div>
<nav class="footer-nav">
  <a style="left:724px">Home</a>
  <a style="left:797px">Tour</a>
  <a style="left:867px">Price</a>
  <a style="left:940px">Our Team</a>
  <a style="left:1037px">Contact Us</a>
</nav>
<div class="footer-rule"></div>
<div class="social" style="left:1021px;background:var(--navy)"></div>
<div class="social" style="left:1053px;background:var(--blue)"></div>
<div class="social" style="left:1084px;background:var(--red)"></div>
<div class="footer-bar"></div>
<p class="copyright">© Copyright 2017 | All Rights Reserved</p>
<nav class="legal">
  <a style="left:830px">Privacy Policy</a>
  <a style="left:920px">Terms &amp; Conditions</a>
  <a style="left:1039px">Refund Policy</a>
</nav>
<div class="to-top">
  <svg width="28" height="28" viewBox="0 0 28 28"><path d="M10.5 15.5l3.5-3.5 3.5 3.5" fill="none" stroke="#fff" stroke-width="1.6"/></svg>
</div>

</body>
</html>
```